Luxury Face Oil Label

I'm looking for a simple and sophisticated design for a natural face oil that will target the luxe market. It is a pure Natural product. I have attached the logo, Velumi Organics.

Here's the Copy

LUXE FACIAL OIL

Regenerate. Hydrate. Glow

100% Natural

30ml (1.01 oz)

A complex blend of Pure Oils including Marula, Sea Buckthorn, Rosehip, Neroli, Evening primrose, Argan, Calendula, Lavender, Jojoba, Grapeseed, Baobab, Moringa and Vitamin E oil.

Produced by
Amber Reedhouse Ltd
P.O box 7925-00300
Nairobi, Kenya
www.velumiorganics.example

Target Market(s)

High end

Requirements
Must have
• Simple, Please consider the bottle, which is a 30ml clear glass bottle with a gold and white pump. Image attached.
Nice to have
• Very clean designs, not too much going on.
Should not have
• Leaves and nuts.

```html
<!DOCTYPE html>
<html lang="en">
<head>
<meta charset="utf-8">
<title>Velumi Organics – Luxe Facial Oil Label</title>
<link rel="stylesheet" href="https://fonts.googleapis.com/css2?family=Montserrat:wght@400;500;700;800&display=swap">
<style>
  :root {
    --page: #f1f1f1;
    --label: #ffffff;
    --gold-deep: #b77f14;
    --gold-text: #b47a14;
    --gold-soft: #f5da7a;
    --gold-light: #fff0a8;
    --ink: #2f2a22;
    --ink-soft: #3a3a3a;
    --logo-ink: #4a4a38;
    --frame: #cfcab8;
    --vein: #f1e8da;
  }
  * { box-sizing: border-box; margin: 0; padding: 0; }
  html, body { width: 1200px; height: 1000px; overflow: hidden; background: var(--page); }
  body { position: relative; font-family: "Montserrat", sans-serif; color: var(--ink); }

  .label {
    position: absolute; left: 30px; top: 170px; width: 1140px; height: 659px;
    background: var(--label); overflow: hidden;
    box-shadow: 0 10px 30px rgba(0,0,0,0.08);
  }
  .marble {
    position: absolute; inset: 0;
    background:
      linear-gradient(160deg, transparent 0%, var(--vein) 30%, transparent 45%),
      linear-gradient(20deg, transparent 55%, var(--vein) 70%, transparent 85%),
      var(--label);
    opacity: 0.7;
  }
  .foliage { position: absolute; }
  .foliage--top { left: 0; top: 15px; width: 320px; height: 160px;
    background: radial-gradient(ellipse at 45% 50%, rgba(214,168,58,0.35), rgba(214,168,58,0) 70%); }
  .foliage--bottom { left: 840px; top: 505px; width: 300px; height: 154px;
    background: radial-gradient(ellipse at 60% 55%, rgba(214,168,58,0.35), rgba(214,168,58,0) 70%); }

  .band { position: absolute; top: 200px; height: 184px; }
  .band--left { left: 0; width: 206px; background: var(--gold-deep); }
  .band--right { left: 493px; width: 647px;
    background: linear-gradient(90deg, #e3bc4f 0%, var(--gold-soft) 30%, var(--gold-light) 50%, #f0d36e 72%, var(--gold-deep) 100%); }

  .brand-box {
    position: absolute; left: 221px; top: 161px; width: 257px; height: 258px;
    background: var(--label); border: 1px solid var(--frame);
    display: flex; align-items: flex-end; justify-content: center; padding-bottom: 52px;
  }
  .brand-box::after {
    content: ""; position: absolute; inset: 6px; border: 1.5px solid var(--frame);
  }
  .brand-name {
    font-family: "Montserrat", sans-serif; font-weight: 400;
    font-size: 22px; letter-spacing: 5px; color: var(--logo-ink);
    text-align: center; line-height: 1.45; text-transform: uppercase;
  }

  .product { position: absolute; left: 150px; width: 400px; text-align: center; }
  .product__name { top: 451px; font-weight: 800; font-size: 31px; color: var(--gold-text); letter-spacing: 0.5px; line-height: 36px; }
  .product__tagline { top: 504px; font-size: 21px; font-weight: 400; color: var(--ink-soft); line-height: 26px; }
  .product__claim { top: 540px; font-weight: 800; font-size: 31px; color: var(--gold-text); line-height: 36px; }
  .product__volume { top: 597px; font-size: 21px; font-weight: 400; color: var(--ink-soft); line-height: 26px; }

  .ingredients-title {
    position: absolute; left: 635px; width: 400px; top: 158px; text-align: center;
    font-weight: 700; font-size: 21px; line-height: 26px; color: var(--gold-text); letter-spacing: 0.3px;
  }
  .ingredients {
    position: absolute; left: 583px; width: 500px; top: 210px; text-align: center;
    font-size: 21px; line-height: 26.6px; color: var(--ink); font-weight: 400;
    white-space: nowrap;
  }
  .producer {
    position: absolute; left: 700px; width: 300px; top: 408px; text-align: center;
    font-size: 18.5px; line-height: 23px; font-weight: 400; color: var(--ink-soft);
  }
</style>
</head>
<body>
  <section class="label">
    <div class="marble" role="img" aria-label="Soft white and cream marble texture"></div>
    <div class="foliage foliage--top" role="img" aria-label="Gold line-drawn leafy branch ornament"></div>
    <div class="foliage foliage--bottom" role="img" aria-label="Gold line-drawn leafy branch ornament"></div>

    <div class="band band--left"></div>
    <div class="band band--right"></div>

    <div class="brand-box">
      <p class="brand-name">Velumi<br>Organics</p>
    </div>

    <h1 class="product product__name">LUXE FACIAL OIL</h1>
    <p class="product product__tagline">Regenerate. Hydrate. Glow</p>
    <p class="product product__claim">100% Natural</p>
    <p class="product product__volume">30ml (1.01 oz)</p>

    <h2 class="ingredients-title">INGREDIENTS</h2>
    <p class="ingredients">A complex blend of Pure Oils<br>including Marula, Sea Buckthorn,<br>Rosehip, Neroli, Evening primrose,<br>Argan, Calendula, Lavender, Jojoba,<br>Grapeseed, Baobab, Moringa and<br>Vitamin E oil.</p>

    <p class="producer">Produced by<br>Amber Reedhouse Ltd<br>P.O box 7925-00300<br>Nairobi, Kenya<br>www.velumiorganics.example</p>
  </section>
</body>
</html>
```